High Profile Web Design Project

We need a sleek,state-of-the-art design for an international real estate company based in the Gulf region.

Fonts should be modern and clean, and a corner should in the top banner should be reserved for the logo.

The logo of the company is gold, navy blue, and white so the website should coincide with this.

The site will actually be an internal portal so it is important that the focus is on content.

This is the first of many requests. Top ten designers will be contacted repeatedly both via the site and privately for further business.

As this is an internal portal for employees, focus should be on news, policies, search, complaints, etc.

Hi All, 

More information on the requirements: 

1- Group Homepage (Do not include department  component like : Department News, Department Blog, Poll, Calendar)

·         Company Announcements

·         Velmora in Press

·         Highlights / Achievements (Three main blocks with photos )

·         Photo Gallery

·         Quick Links (Trackon – Ledgrix – Organization Structure – Phone Directory …)

·         Navigation tabs
- Properties (Include sub links for departments)
-International (Include sub links for countries list)
-  Hospitality (Include sub links for hotels)
- Retail (Include sub links for attractions)
- Malls Group (Include sub links for malls)
- Technologies

 

2-      Department Homepage (Information technology for example but can be applied for Finance, HR, Marketing, Mall, Hotel…etc)

·         Department Announcements

·         Technology News

·         Project Office

·         Quick Links (Trackon – Ledgrix – IT Policies – Activity Calendar …)

·         Department Blog

·         Poll (Best Project – Employee of the month – Best Photography)... one poll  at time

 

Target Market(s)

real-estate employees

Industry/Entity Type

Real Estate

Requirements
Must have
• - Space in the corner for the logo (which is a square logo);
- Colors which match with navy blue & gold;
- Content centric design;
Should not have
• Scrolling - we want to try to limit the need for scrolling - especially on the portal home page.

```html
<!DOCTYPE html>
<html lang="en">
<head>
<meta charset="utf-8">
<title>Velmora Group Portal</title>
<link href="https://fonts.googleapis.com/css2?family=Arimo:wght@400;700&family=Great+Vibes&display=swap" rel="stylesheet">
<style>
:root{
  --page:#cfcfcf;
  --panel:#6c6c6c;
  --panel-dark:#2a2a2a;
  --silver-hi:#e4e4e4;
  --silver-lo:#8d8d8d;
  --navy:#1c2a8a;
  --navy-deep:#0d1650;
  --gold:#e2d21a;
  --gold-soft:#cfc21e;
  --text:#ffffff;
  --tile:#2b2b2b;
  --tile-text:#7a7a7a;
  --footer-text:#1e1e1e;
}
*{margin:0;padding:0;box-sizing:border-box}
html,body{width:1200px;height:773px;overflow:hidden}
body{background:var(--page);font-family:"Arimo",Arial,sans-serif;color:var(--text);position:relative}
.panel{position:absolute;left:38px;top:0;width:1132px;height:773px;
  background:linear-gradient(90deg,#1e1e1e 0,var(--panel) 40px,var(--panel) 1092px,#1e1e1e 100%)}
.abs{position:absolute}
.header-bar{left:147px;top:0;width:913px;height:66px;border-radius:0 0 8px 0;
  background:linear-gradient(180deg,var(--silver-hi),var(--silver-lo));box-shadow:0 3px 4px rgba(0,0,0,.5)}
.logo-tab{left:147px;top:0;width:230px;height:132px;border-radius:0 0 10px 18px;
  background:linear-gradient(180deg,var(--silver-hi),#7e7e7e);box-shadow:0 3px 5px rgba(0,0,0,.5)}
.header-rule{left:371px;top:77px;width:689px;height:4px;background:#2c2c2c}
.logo{left:183px;top:11px;width:110px;height:110px;border:3px solid var(--gold);border-radius:8px;
  background:linear-gradient(180deg,var(--navy),var(--navy-deep));display:flex;align-items:center;justify-content:center;
  font-size:19px;color:var(--gold)}
.nav{left:380px;top:35px;display:flex;list-style:none}
.nav li{position:absolute;top:0;font-size:12.5px;font-weight:700;letter-spacing:1.3px;text-transform:uppercase;color:#fff;
  text-shadow:0 1px 1px #333;white-space:nowrap}
.nav li::after{content:"";position:absolute;left:50%;top:18px;margin-left:-3px;border:4px solid transparent;border-top:5px solid var(--gold)}
.banner{left:143px;top:96px;width:923px;height:193px;border:3px solid #fff;border-radius:14px 4px 14px 4px;overflow:hidden;
  background:linear-gradient(180deg,#2f52c4 0,#223a9c 55%,#0e1a5a 100%)}
.banner-title{left:217px;top:6px;font-family:"Great Vibes",cursive;font-size:50px;color:var(--gold)}
.banner-sub{left:149px;top:58px;font-size:20px;color:#8f96b5}
.banner-scene{left:0;bottom:0;width:100%;height:80px;background:linear-gradient(180deg,rgba(10,20,70,0),rgba(8,14,50,.85))}
.banner-house{left:630px;top:20px;width:180px;height:145px;border-radius:6px;background:linear-gradient(160deg,#f3e99a,#c9b636)}
h2{position:absolute;font-size:17px;font-weight:400;color:var(--gold);text-shadow:1px 1px 1px #222;letter-spacing:.3px}
.copy{position:absolute;font-size:12px;line-height:13px;text-align:justify;letter-spacing:.3px}
.more{color:var(--gold);font-size:12px;float:right}
.icon{background:linear-gradient(180deg,#e8dc52,#9c9120);border-radius:6px}
.rule{position:absolute;height:2px;background:var(--gold-soft)}
.tile{position:absolute;background:var(--tile);box-shadow:2px 3px 4px rgba(0,0,0,.55);display:flex;align-items:flex-end;justify-content:center;
  color:var(--tile-text);font-size:16px;letter-spacing:1px;padding-bottom:20px}
.tile-caption{position:absolute;width:100px;font-size:10.5px;line-height:11px;text-align:justify}
.tile-more{position:absolute;font-size:11px;color:var(--gold)}
.press-photo{left:537px;top:331px;width:205px;height:84px;border:3px solid #2a2a2a;
  background:linear-gradient(180deg,#3d78d0,#9cc0ea 60%,#5d6a7a)}
.quick{position:absolute;left:844px;width:232px;font-size:11.5px;line-height:17px;letter-spacing:.2px}
.quick .lead{color:var(--gold)}
.quick .more{font-size:11.5px}
.footer-nav{left:0;top:704px;width:1200px;display:flex;justify-content:center;list-style:none;font-size:10.5px;color:var(--footer-text)}
.footer-nav li{padding:0 5px;border-left:2px solid var(--gold)}
.footer-nav li:first-child{border-left:0}
.legal{left:0;top:726px;width:1200px;text-align:center;font-size:10px;color:var(--footer-text);letter-spacing:.3px}
</style>
</head>
<body>
<div class="panel"></div>

<header>
  <div class="abs header-bar"></div>
  <div class="abs logo-tab"></div>
  <div class="abs header-rule"></div>
  <div class="abs logo">Velmora</div>
  <ul class="abs nav">
    <li style="left:9px">Properties</li>
    <li style="left:123px">International</li>
    <li style="left:268px">Hospitality</li>
    <li style="left:391px">Retail</li>
    <li style="left:473px">Malls</li>
    <li style="left:546px">Technologies</li>
  </ul>
</header>

<section class="abs banner">
  <div class="abs banner-scene" role="img" aria-label="Night city skyline"></div>
  <div class="abs banner-house" role="img" aria-label="Golden house illustration"></div>
  <div class="abs banner-title">The real Estate</div>
  <div class="abs banner-sub">Lorem ipsum dolor sit amet</div>
</section>

<main>
  <!-- Announcements -->
  <div class="abs icon" style="left:134px;top:316px;width:46px;height:54px" role="img" aria-label="Megaphone icon"></div>
  <h2 style="left:189px;top:304px">Company Announcements</h2>
  <p class="copy" style="left:191px;top:325px;width:313px">Lorem ipsum dolor sit amet, consectetur adipiscing elit. Duis fringilla arcu erat, eget hendrerit neque. In pretium interdum dolor, lobortis molestie libero euismod nec. Maecenas malesuada tempus magna a laoreet. Sedid.<br><span class="more">Read More...</span></p>
  <div class="rule" style="left:221px;top:406px;width:226px"></div>

  <div class="abs icon" style="left:134px;top:424px;width:42px;height:58px" role="img" aria-label="Number one trophy icon"></div>
  <h2 style="left:191px;top:415px">Highlights &amp; Achievements</h2>
  <p class="copy" style="left:192px;top:434px;width:313px">Lorem ipsum dolor sit amet, consectetur adipiscing elit. Duis fringilla arcu erat, eget hendrerit neque. In pretium interdum dolor, lobortis molestie libero euismod nec. Maecenas malesuada tempus magna a laoreet. Sedid.<br><span class="more">Read More...</span></p>

  <div class="tile" style="left:142px;top:513px;width:99px;height:78px">Image</div>
  <div class="tile" style="left:268px;top:514px;width:100px;height:78px">Image</div>
  <div class="tile" style="left:403px;top:514px;width:100px;height:78px">Image</div>
  <p class="tile-caption" style="left:141px;top:602px">Lorem ipsum dolor sit amet, consectetur adipiscing elit. Duis fringilla arcu erat, eget hendrerit neque. In prtium intedum</p>
  <p class="tile-caption" style="left:272px;top:600px">Lorem ipsum dolor sit amet, consectetur adipiscing elit. Duis fringilla arcu erat, eget hendrerit neque. In prtium intedum</p>
  <p class="tile-caption" style="left:404px;top:600px">Lorem ipsum dolor sit amet, consectetur adipiscing elit. Duis fringilla arcu erat, eget hendrerit neque. In prtium intedum</p>
  <span class="tile-more" style="left:175px;top:672px">read more...</span>
  <span class="tile-more" style="left:306px;top:670px">read more...</span>
  <span class="tile-more" style="left:437px;top:670px">read more...</span>

  <!-- Press -->
  <h2 style="left:537px;top:307px">Velmora in Press</h2>
  <div class="abs press-photo" role="img" aria-label="City skyline with billboard"></div>
  <p class="copy" style="left:538px;top:419px;width:255px">Lorem ipsum dolor sit amet, consectetur adipiscing elit. Duis fringilla arcu erat, eget hendrerit neque. In pretium interdum dolor,<span class="more">Read More...</span></p>
  <div class="rule" style="left:554px;top:474px;width:226px"></div>

  <h2 style="left:537px;top:478px">Photo Gallery</h2>
  <svg class="abs" style="left:541px;top:516px" width="78" height="66" viewBox="0 0 78 66" aria-hidden="true">
    <ellipse cx="39" cy="33" rx="34" ry="26" fill="none" stroke="#d8cc1e" stroke-width="6"/>
  </svg>
  <div class="tile" style="left:633px;top:502px;width:84px;height:78px">Image</div>
  <div class="tile" style="left:723px;top:502px;width:85px;height:78px">Image</div>
  <div class="tile" style="left:538px;top:593px;width:84px;height:79px">Image</div>
  <div class="tile" style="left:632px;top:593px;width:84px;height:79px">Image</div>
  <div class="tile" style="left:724px;top:593px;width:84px;height:79px">Image</div>

  <!-- Quick links -->
  <h2 style="left:839px;top:309px">Quick Links</h2>
  <div class="quick" style="top:332px"><div class="lead">Lorem ipsum dolor sit amet, consectetur</div>Lorem ipsum dolor sit amet, consectetur<br>adipiscing elit.<span class="more">Read More...</span></div>
  <div class="rule" style="left:844px;top:389px;width:226px"></div>
  <div class="quick" style="top:396px"><div class="lead">Lorem ipsum dolor sit amet, consectetur</div>Lorem ipsum dolor sit amet, consectetur<br>adipiscing elit.<span class="more">Read More...</span></div>
  <div class="rule" style="left:844px;top:451px;width:226px"></div>
  <div class="quick" style="top:454px"><div class="lead">Lorem ipsum dolor sit amet, consectetur</div>Lorem ipsum dolor sit amet, consectetur<br>adipiscing elit.<span class="more">Read More...</span></div>
  <div class="rule" style="left:844px;top:514px;width:226px"></div>
  <div class="quick" style="top:522px;left:847px"><div class="lead">Lorem ipsum dolor sit amet, consectetur</div>Lorem ipsum dolor sit amet, consectetur<br>adipiscing elit.<span class="more">Read More...</span></div>
  <div class="rule" style="left:847px;top:586px;width:226px"></div>
  <div class="quick" style="top:589px;left:849px"><div class="lead">Lorem ipsum dolor sit amet, consectetur</div>Lorem ipsum dolor sit amet, consectetur<br>adipiscing elit.<span class="more">Read More...</span></div>
  <div class="rule" style="left:849px;top:654px;width:226px"></div>
</main>

<footer>
  <ul class="abs footer-nav">
    <li>Blog</li><li>Support</li><li>Solutions</li><li>Testimonials</li><li>Developments</li><li>Projects</li><li>Contact Us</li>
  </ul>
  <p class="abs legal">©2012 Your Company. All Rights Reserved</p>
</footer>
</body>
</html>
```